National online rug retailer needs a home page design

See the MatsNowly logo and create a home page design around that color theme. Details are spelled out in word document uploaded below.

Apparently this website did not take my attachement showing the logo and basic requirements.  If you would send me your email address, I will send you the attachment directly.
Best regards,
Ned Ferris
nferris@qorvex.com

Target Market(s)

The target market is home owners 25 to 75 years old with combined incomes over $100,000 per year.

Industry/Entity Type

Online

Requirements
Must have
• Lots of white space with black letters and creative use of red and possibly one other color. Would like a compelling call to action button.

```html
<!DOCTYPE html>
<html lang="en">
<head>
<meta charset="utf-8">
<title>MatsNowly – Home</title>
<link rel="stylesheet" href="https://fonts.googleapis.com/css2?family=Cinzel:wght@400;500&family=PT+Serif&family=Roboto:wght@300;400;700;900&display=swap">
<style>
:root{
  --red:#e0001b;
  --red-deep:#c5001a;
  --ink:#1c1c1c;
  --grey-text:#666;
  --panel:#ececec;
  --footer:#e9e9e9;
  --teal:#5f95a8;
  --blue-accent:#2a9fd0;
  --fringe:#c9b48a;
  --white:#fff;
}
*{box-sizing:border-box;margin:0;padding:0}
html,body{width:833px;height:1200px;overflow:hidden;background:var(--white)}
body{position:relative;font-family:"Roboto",sans-serif;color:var(--ink)}
.abs{position:absolute}

/* header */
.top-rule{left:0;top:0;width:833px;height:4px;background:var(--red)}
.site-header{left:0;top:4px;width:833px;height:89px;border-bottom:1px solid #ddd}
.brand-name{font-family:"Roboto",sans-serif;font-weight:400;font-size:32px;color:var(--red);display:flex;align-items:center;gap:7px;letter-spacing:-.5px}
.brand-name .mark{width:12px;height:12px;background:var(--red)}
.brand-tag{font-size:9px;color:#444;margin-left:68px;margin-top:1px}
.nav a{position:absolute;top:44px;font-size:16px;font-weight:300;color:#555;text-decoration:none;letter-spacing:.2px}
.nav .active{color:var(--red)}
.nav-underline{left:403px;top:87px;width:61px;height:6px;background:var(--red)}
.nav-sep{top:8px;width:1px;height:85px;background:#e2e2e2}

/* hero */
.hero{left:0;top:103px;width:833px;height:216px}
.hero-rugs{left:0;top:0;width:252px;height:216px;background:linear-gradient(135deg,#6e7a2c 0%,#8d9b3a 45%,#c9402a 60%,#6e7a2c 100%)}
.hero-room{left:252px;top:0;width:316px;height:216px;background:linear-gradient(180deg,#4a5a3a 0%,#7a8a5a 30%,#8fa060 75%,#5e7038 100%)}
.hero-band{left:252px;top:63px;width:316px;height:94px;background:rgba(235,235,230,.82)}
.hero-band .best{position:absolute;left:18px;top:24px;font:900 23px/1 "Roboto",sans-serif;color:var(--red)}
.hero-band .coll{position:absolute;left:29px;top:46px;font:700 19px/1 "Roboto",sans-serif;color:#111}
.hero-band .coll small{font-size:8.5px;font-weight:700}
.tiles{left:568px;top:0;width:265px;height:216px;display:grid;grid-template-columns:90px 91px 84px;grid-template-rows:63px 96px 57px}
.tiles div{border:1px solid #fff}
.t1{background:#3c7c7e}.t2{background:#3d93b0}.t3{background:linear-gradient(180deg,#7aa0a5,#c2523b,#e6c36a)}
.t4{background:#4d93ad}
.t5{background:linear-gradient(180deg,#f2c14a 0%,#8fb84a 50%,#2a8fc8 100%)}
.t6{background:#8c8b86}.t7{background:#e8601e}.t8{background:#b88a3a}.t9{background:linear-gradient(135deg,#e33b6b,#f3a32a,#2aa9c8)}
.red-band{left:0;top:320px;width:833px;height:58px;background:radial-gradient(ellipse 260px 40px at 50% 10%,#ff3b3b 0%,var(--red) 45%,#c8000f 100%)}

/* offers strip */
.deals{left:0;top:378px;width:833px;height:192px;background:var(--panel);border-bottom:1px solid #d6d6d6}
.deal-sep{top:0;width:1px;height:192px;background:#d6d6d6}
.deal-label{font:400 25px/1 "Cinzel",serif;color:#222}
.deal-pct{font:400 46px/1 "Roboto",sans-serif;color:var(--red)}
.deal-arrow{width:0;height:0;border-top:11px solid transparent;border-bottom:11px solid transparent;border-left:12px solid #333}
.deal-active{left:92px;top:565px;width:166px;height:3px;background:#333}

/* content row */
.card{top:588px;height:279px}
.panel h2{font:400 16px/1 "Roboto",sans-serif;padding:17px 18px 13px;border-bottom:1px solid rgba(255,255,255,.45)}
.panel p{font-size:12.4px;line-height:14.5px;font-weight:400}
.about{left:87px;width:173px;background:var(--teal)}
.about h2{color:#fff}
.about p{color:#10252c;margin-top:11px;padding:0 22px 0 14px}
.about p+p{margin-top:10px}
.tasting{left:260px;top:588px;width:168px;height:140px;background:#fff}
.tasting h2{font-size:16px;border:none;padding:18px 11px 12px;color:#111}
.tasting p,.tasting2 p{color:var(--grey-text);padding:0 11px}
.photo-rug{left:428px;top:588px;width:167px;height:138px;background:linear-gradient(135deg,#5a3a22 0%,#6e4a2a 35%,#222 50%,#e8e2c8 60%,#222 80%,#c9b55a 100%)}
.photo-bed{left:260px;top:728px;width:168px;height:139px;background:linear-gradient(180deg,#9a9d96 0%,#b4b5ad 55%,#d8d6cd 100%)}
.tasting2{left:428px;top:726px;width:167px;height:141px;background:#fff}
.tasting2 h2{font-size:12.5px;border:none;padding:17px 12px 13px;color:#111}
.tasting2 p{padding:0 12px}
.notch{left:502px;top:718px;width:0;height:0;border-left:9px solid transparent;border-right:9px solid transparent;border-bottom:9px solid #fff}
.offers-card{left:595px;width:173px;background:var(--red-deep)}
.offers-card h2{color:#fff}
.offers-card p{color:#fff;margin-top:9px;padding:0 21px 0 14px}
.fringe{top:867px;width:173px;height:14px;background:var(--fringe)}

/* lower section */
.bracket{width:23px;height:23px}
.change-title{left:242px;top:920px;font:400 14px/1 "PT Serif",serif;color:var(--red);letter-spacing:.6px}
.change-quote{left:241px;top:953px;width:215px;font-size:8.6px;line-height:11.5px;color:#222}
.demo{left:382px;top:1010px;font:400 9px/1 "PT Serif",serif;letter-spacing:.5px;color:#222}
.rolled-rug{left:140px;top:953px;width:86px;height:63px;background:linear-gradient(160deg,#7fb0b3,#5f9296);border-radius:6px;transform:skewY(-14deg)}
.divider-v{left:471px;top:890px;width:1px;height:170px;background:#ddd}
.news-photo{left:509px;top:941px;width:70px;height:72px;background:linear-gradient(135deg,#6a5a4a,#b9a184 55%,#c93a3a)}
.news-title{left:599px;top:926px;font:400 12px/1 "PT Serif",serif;color:var(--red)}
.news-text{left:603px;top:954px;font-size:8px;line-height:11px;color:#222}
.news-q{left:636px;top:985px;font:300 36px/1 "Roboto",sans-serif;color:var(--blue-accent)}

/* footer */
.footer{left:0;top:1060px;width:833px;height:112px;background:var(--footer)}
.foot-brand{left:96px;top:1108px;font-size:13px;color:var(--red);display:flex;align-items:center;gap:4px}
.foot-brand .mark{width:6px;height:6px;background:var(--red)}
.foot-tag{left:122px;top:1124px;font-size:3.6px;color:#555}
.foot-h{font:400 9px/1 "PT Serif",serif;letter-spacing:.6px;color:#222}
.foot-links{font-size:7px;line-height:14px;color:#555}
.foot-menu{left:309px;top:1108px;width:145px;font-size:6.8px;line-height:8.6px;color:#555}
.branch{font-size:6.8px;line-height:8px;color:#555}
.copyright{left:308px;top:1183px;font-size:6.6px;color:var(--blue-accent);letter-spacing:.2px}
.social{top:1181px}
</style>
</head>
<body>

<div class="abs top-rule"></div>
<header class="abs site-header">
  <div class="abs" style="left:87px;top:20px">
    <div class="brand-name"><span class="mark"></span>MatsNowly</div>
    <div class="brand-tag">for domestic and heirloom values</div>
  </div>
  <nav class="nav">
    <a class="active" style="left:410px">HOME</a>
    <a style="left:496px">OFFERS</a>
    <a style="left:580px">CONTACT US</a>
    <a style="left:695px">MENU</a>
  </nav>
  <div class="abs nav-sep" style="left:484px"></div>
  <div class="abs nav-sep" style="left:569px"></div>
  <div class="abs nav-sep" style="left:678px"></div>
</header>
<div class="abs nav-underline"></div>

<section class="abs hero">
  <div class="abs hero-rugs" role="img" aria-label="Rolled patterned rugs lying on a green and red rug"></div>
  <div class="abs hero-room" role="img" aria-label="Living room with a sofa above a green pebble-pattern rug"></div>
  <div class="abs hero-band">
    <div class="best">BEST</div>
    <div class="coll">COLLECTIONS<small> YOU CAN FIND EVER</small></div>
  </div>
  <div class="abs tiles">
    <div class="t1" role="img" aria-label="Circle pattern rug swatch"></div>
    <div class="t2" role="img" aria-label="Blue rug swatch"></div>
    <div class="t3" role="img" aria-label="Striped rug swatch"></div>
    <div class="t4" role="img" aria-label="Blue textured rug swatch"></div>
    <div class="t5" role="img" aria-label="Lettered graphic: rugs under 100 dollars"></div>
    <div class="t6" role="img" aria-label="Grey rug swatch"></div>
    <div class="t7" role="img" aria-label="Orange circle rug swatch"></div>
    <div class="t8" role="img" aria-label="Woven tan rug swatch"></div>
    <div class="t9" role="img" aria-label="Colourful wave rug swatch"></div>
  </div>
</section>
<div class="abs red-band"></div>

<section class="abs deals">
  <div class="abs deal-sep" style="left:258px"></div>
  <div class="abs deal-sep" style="left:532px"></div>
  <div class="abs deal-label" style="left:96px;top:43px">2 RUGS</div>
  <div class="abs deal-pct" style="left:160px;top:66px">10%</div>
  <div class="abs deal-arrow" style="left:260px;top:72px"></div>
  <div class="abs deal-label" style="left:320px;top:43px">3 RUGS</div>
  <div class="abs deal-pct" style="left:407px;top:76px">15%</div>
  <div class="abs deal-arrow" style="left:534px;top:72px"></div>
  <div class="abs deal-label" style="left:554px;top:43px">5 RUGS</div>
  <div class="abs deal-pct" style="left:625px;top:81px">25%</div>
</section>
<div class="abs deal-active"></div>

<section class="abs card panel about">
  <h2>About us</h2>
  <p>Dummy data is benign information that does not contain any useful data, but serves to re-serve space where real data is nominally pre-sent.</p>
  <p>Dummy data is benign information any useful dataset.</p>
  <p>Dummy data is benign dataset.</p>
</section>
<div class="abs fringe" style="left:87px" role="img" aria-label="Rug fringe"></div>

<section class="abs panel tasting">
  <h2>BEST TASTING EVER</h2>
  <p>benign information that does not contain any usefubenign information that does not contain any usefu</p>
</section>
<div class="abs photo-rug" role="img" aria-label="Black and white zigzag rug beside a wooden table"></div>
<div class="abs photo-bed" role="img" aria-label="Bedroom with an upholstered bed and chandelier"></div>
<section class="abs panel tasting2">
  <h2>BEST TASTING EVER</h2>
  <p>benign information that does not contain any usefubenign information that does not contain any usefu</p>
</section>
<div class="abs notch"></div>

<section class="abs card panel offers-card">
  <h2>OFFERS</h2>
  <p>Dummy data is benign information that does not contain any useful data, but serves to re-serve space where real data is nominally pre-sent. Dummy data can be used as cholder for both not contain any useful data, but serves to reserve space where real data is nominally present. Dummy data can be used as cholder for both &nbsp;testing .</p>
</section>
<div class="abs fringe" style="left:595px" role="img" aria-label="Rug fringe"></div>

<svg class="abs bracket" style="left:132px;top:915px" viewBox="0 0 23 23"><path d="M1 23V1h22" fill="none" stroke="#2a9fd0" stroke-width="2"/></svg>
<svg class="abs bracket" style="left:209px;top:1021px" viewBox="0 0 23 23"><path d="M0 22h22V0" fill="none" stroke="#222" stroke-width="2"/></svg>
<div class="abs rolled-rug" role="img" aria-label="Rolled teal rug with leaf border"></div>
<div class="abs change-title">HOW CAN YOU CHANGE</div>
<div class="abs change-quote">"We go to extraordinary lengths to provide world-class healthcare staffing and believe we can help achieve real improvements in patient care."</div>
<div class="abs demo">WATCH DEMO</div>

<div class="abs divider-v"></div>

<svg class="abs bracket" style="left:495px;top:932px" viewBox="0 0 23 23"><path d="M1 23V1h22" fill="none" stroke="#e0001b" stroke-width="2"/></svg>
<svg class="abs bracket" style="left:575px;top:1002px" viewBox="0 0 23 23"><path d="M0 22h22V0" fill="none" stroke="#222" stroke-width="2"/></svg>
<div class="abs news-photo" role="img" aria-label="Person standing beside a hanging rug"></div>
<div class="abs news-title">NEWS</div>
<div class="abs news-text">What's going on<br>in our world</div>
<div class="abs news-q">?</div>

<footer class="abs footer"></footer>
<div class="abs foot-brand"><span class="mark"></span>MatsNowly</div>
<div class="abs foot-tag">for domestic and heirloom values</div>
<div class="abs foot-h" style="left:204px;top:1091px">HOME</div>
<div class="abs foot-links" style="left:204px;top:1105px">ABOUT<br>SERVICES<br>CONTACT US</div>
<div class="abs foot-h" style="left:309px;top:1091px">MENU</div>
<div class="abs foot-menu">benign any useful data, but serves to reserve space enign any useful data, but serves to reserve space where real data is nominally......</div>
<div class="abs foot-h" style="left:480px;top:1091px">BRANCH</div>
<svg class="abs" style="left:479px;top:1108px" width="9" height="9" viewBox="0 0 10 10"><path d="M5 0a3.5 3.5 0 0 1 3.5 3.5C8.5 6 5 10 5 10S1.5 6 1.5 3.5A3.5 3.5 0 0 1 5 0z" fill="#222"/><circle cx="5" cy="3.5" r="1.3" fill="#e9e9e9"/></svg>
<div class="abs branch" style="left:500px;top:1111px">12 Lindenweg, Hallbrook</div>
<svg class="abs" style="left:479px;top:1128px" width="9" height="10" viewBox="0 0 10 10"><path d="M5 0a3.5 3.5 0 0 1 3.5 3.5C8.5 6 5 10 5 10S1.5 6 1.5 3.5A3.5 3.5 0 0 1 5 0z" fill="#222"/><circle cx="5" cy="3.5" r="1.3" fill="#e9e9e9"/></svg>
<div class="abs branch" style="left:500px;top:1130px">BRANCH2: 48 Corran Street,<br>Westmoor</div>

<div class="abs copyright">ALL RIGHTS RESERVED 2013 &nbsp;TERMS OF USE</div>
<svg class="abs social" style="left:709px" width="8" height="8" viewBox="0 0 8 8"><circle cx="4" cy="4" r="3.5" fill="#2a9fd0"/></svg>
<svg class="abs social" style="left:727px" width="10" height="9" viewBox="0 0 10 9"><path d="M1 4.5L5 1l4 3.5M2.5 3.5V8h5V3.5" fill="none" stroke="#2a9fd0" stroke-width="1.3"/></svg>
<svg class="abs social" style="left:747px" width="9" height="9" viewBox="0 0 9 9"><circle cx="3.6" cy="3.6" r="2.6" fill="none" stroke="#2a9fd0" stroke-width="1.3"/><path d="M5.5 5.5L8.5 8.5" stroke="#2a9fd0" stroke-width="1.5"/></svg>

</body>
</html>
```